Flyer for New Spa Opening

We need a flyer to increase customer's awareness of our new spa located in Yangon, Myanmar, in a middle-upper class shopping mall. A new hotel will be opening above the mall in Dec 2013.
Updates

Have made payment guaranteed.  Need a good flyer. Thanks.

Hi, I have uploaded a Words File for Flyer Text. Thanks!

Dear Designers,

I have setup a 2nd award, there's too many outstanding designs! Thanks so much.

Regards
Odile

Target Market(s)

-Hotel guest who wants to a spa session to relax
-Woman between 18 - 55 years old who have high spending power in a poor country(Myanmar). They like to use "Big Brands" but do not have much variety available in their country.

Industry/Entity Type

Shopping

Requirements
Must have
• Our services include Body Spa, Facial, Nails, Waxing & Foot Reflexology. We use well-known international brands in our spa including Veloranthe, KUV, Marven, Brenzo Lativa and TORVE.

Veloranthe, the skin care system researched and developed by The Halvering Dermal Academy (HDA), is an international leader in today’s skin care industry.

We are authorized Veloranthe skin spa to provide professional facial and retailing Veloranthe products.

Include the logo of the brands

Quellmoor Spa
add: No 82, Kelvash Road, Morrin Plaza (Level-5) (7168), Dagon Township, Yangon
tel: +959 62087315
email: contactus@vertlane-holdco.example

Nice to have
• visually nice and relaxing spa pictures.
Should not have
• price

```html
<!DOCTYPE html>
<html lang="en">
<head>
<meta charset="utf-8">
<title>Quellmoor Spa – Flyer</title>
<link rel="stylesheet" href="https://fonts.googleapis.com/css2?family=Great+Vibes&family=Didact+Gothic&display=swap">
<style>
  :root {
    --teal: #1c93b5;
    --white: #ffffff;
    --ink: #1e1e1e;
    --body-text: #2b2b2b;
    --brand-grey: #707070;
    --shadow-grey: #4a4a4a;
    --rule-grey: #6a6a6a;
    --skin-light: #f4dccb;
    --skin-mid: #e6b999;
    --stone-light: #efe4d2;
    --stone-mid: #d6c0a2;
  }
  html, body {
    margin: 0;
    padding: 0;
    overflow: hidden;
    background: var(--white);
  }
  .flyer {
    position: relative;
    width: 1200px;
    height: 851px;
    overflow: hidden;
    background: var(--white);
    font-family: "Didact Gothic", "Century Gothic", sans-serif;
    color: var(--body-text);
  }
  .script {
    font-family: "Great Vibes", cursive;
    font-weight: 400;
    line-height: 1;
  }

  /* ---------- left panel: waxing ---------- */
  .waxing-title {
    position: absolute;
    left: 36px;
    top: 44px;
    margin: 0;
    font-size: 46px;
    color: var(--teal);
  }
  .waxing-copy {
    position: absolute;
    left: 36px;
    top: 114px;
    width: 345px;
    margin: 0;
    font-size: 13.3px;
    line-height: 19px;
    color: var(--body-text);
  }
  .waxing-visual {
    position: absolute;
    left: 0;
    top: 150px;
    width: 420px;
    height: 480px;
  }

  .brand-name {
    position: absolute;
    margin: 0;
    font-weight: 400;
    color: var(--ink);
    white-space: nowrap;
    line-height: 1;
  }
  .brand-brenzo { left: 24px; top: 694px; font-size: 20px; }
  .brand-torve { left: 168px; top: 690px; font-size: 26px; }
  .brand-kuv { left: 272px; top: 686px; font-size: 32px; }
  .brand-lead {
    left: 36px;
    top: 782px;
    font-size: 44px;
    color: var(--brand-grey);
  }

  /* ---------- centre panel ---------- */
  .centre-band-top {
    position: absolute;
    left: 404px;
    top: 0;
    width: 396px;
    height: 529px;
    background: var(--teal);
  }
  .centre-band-bottom {
    position: absolute;
    left: 404px;
    top: 724px;
    width: 396px;
    height: 127px;
    background: var(--teal);
  }
  .centre-title {
    position: absolute;
    left: 455px;
    top: 154px;
    margin: 0;
    font-size: 58px;
    color: var(--white);
    white-space: nowrap;
  }
  .centre-tagline {
    position: absolute;
    left: 455px;
    top: 220px;
    margin: 0;
    font-size: 16px;
    color: var(--white);
  }
  .contact {
    position: absolute;
    left: 404px;
    top: 586px;
    width: 396px;
    margin: 0;
    font-style: normal;
    text-align: center;
    font-size: 13.3px;
    line-height: 18.5px;
    color: var(--ink);
  }

  /* ---------- right panel ---------- */
  .cover-block-shadow {
    position: absolute;
    left: 940px;
    top: 123px;
    width: 204px;
    height: 202px;
    background: var(--shadow-grey);
  }
  .cover-block {
    position: absolute;
    left: 860px;
    top: 0;
    width: 280px;
    height: 321px;
    background: var(--teal);
  }
  .cover-title {
    position: absolute;
    left: 850px;
    top: 362px;
    margin: 0;
    font-size: 58px;
    color: var(--teal);
    white-space: nowrap;
  }
  .cover-tagline {
    position: absolute;
    left: 851px;
    top: 428px;
    margin: 0;
    font-size: 16px;
    color: var(--teal);
  }
  .cover-rule {
    position: absolute;
    left: 800px;
    width: 400px;
    height: 2px;
    background: var(--rule-grey);
  }
  .cover-rule-top { top: 530px; }
  .cover-rule-bottom { top: 722px; }
  .stone-massage-visual {
    position: absolute;
    left: 800px;
    top: 532px;
    width: 400px;
    height: 190px;
    background: linear-gradient(180deg, var(--stone-light) 0%, var(--skin-light) 55%, var(--stone-mid) 100%);
  }
</style>
</head>
<body>
<main class="flyer">

  <section class="panel-waxing">
    <h2 class="waxing-title script">Waxing</h2>
    <p class="waxing-copy">We take care of all the unsightly hairy body parts, just leave it to us. Walk out like a new sexy you!</p>

    <svg class="waxing-visual" viewBox="0 150 420 480" role="img" aria-label="Photograph of smooth bare legs rising from water, scattered with red rose petals">
      <defs>
        <clipPath id="waxing-circle-clip">
          <circle cx="178" cy="390" r="226"/>
        </clipPath>
        <linearGradient id="waxing-tones" x1="0" y1="0" x2="0" y2="1">
          <stop offset="0" stop-color="#ffffff"/>
          <stop offset="0.35" stop-color="#f7e6da"/>
          <stop offset="0.6" stop-color="#e6b999"/>
          <stop offset="0.82" stop-color="#f3e9e4"/>
          <stop offset="1" stop-color="#ffffff"/>
        </linearGradient>
      </defs>
      <rect x="0" y="150" width="420" height="480" fill="url(#waxing-tones)" clip-path="url(#waxing-circle-clip)"/>
      <circle cx="178" cy="390" r="226" fill="none" stroke="#1c93b5" stroke-width="3"/>
      <path d="M404 268 A 232 232 0 0 1 404 512" fill="none" stroke="#1c93b5" stroke-width="2"/>
    </svg>

    <p class="brand-name brand-brenzo">Brenzo Lativa</p>
    <p class="brand-name brand-torve">TORVE</p>
    <p class="brand-name brand-kuv">KUV</p>
    <p class="brand-name brand-lead">Veloranthe</p>
  </section>

  <section class="panel-contact">
    <div class="centre-band-top"></div>
    <h2 class="centre-title script">Quellmoor Spa</h2>
    <p class="centre-tagline">your relaxation is our goal</p>

    <address class="contact">
      Address: No 82, Kelvash Road, Morrin Plaza<br>
      (Level-5) (7168), Dagon Township, Yangon<br>
      Tel: +959 62087315<br>
      Email: contactus@vertlane-holdco.example
    </address>

    <div class="centre-band-bottom"></div>
  </section>

  <section class="panel-cover">
    <div class="cover-block-shadow"></div>
    <div class="cover-block"></div>
    <h1 class="cover-title script">Quellmoor Spa</h1>
    <p class="cover-tagline">your relaxation is our goal</p>

    <div class="cover-rule cover-rule-top"></div>
    <div class="stone-massage-visual" role="img" aria-label="Photograph of a woman relaxing face-down during a hot stone massage"></div>
    <div class="cover-rule cover-rule-bottom"></div>
  </section>

</main>
</body>
</html>
```